A business selling natural soaps online and in farmers markets. I want it to reflect local commerce and natural lifestyle. My colors are olive green and saddle brown. I want the dimensions to be 2.25 x 3.25" with matte finish.
Updates

The name of my company is Fern Hollow Soapworks, LLC

Industry/Entity Type

Business

```html
<!DOCTYPE html>
<html lang="en">
<head>
<meta charset="utf-8">
<title>Fern Hollow Soapworks, LLC — Business Cards</title>
<link rel="stylesheet" href="https://fonts.googleapis.com/css2?family=Open+Sans:wght@400;600&display=swap">
<style>
  :root {
    --backdrop: #e4e4e4;
    --card-paper: #efe9d5;
    --olive: #6fa64e;
    --saddle: #8a3b17;
    --band-text: #f3eedd;
  }
  * { margin: 0; padding: 0; box-sizing: border-box; }
  html, body { width: 1200px; height: 777px; overflow: hidden; }
  body {
    background: var(--backdrop);
    font-family: "Open Sans", Arial, sans-serif;
    position: relative;
  }
  .card {
    position: absolute;
    top: 208px;
    width: 520px;
    height: 360px;
    background: var(--card-paper);
    overflow: hidden;
    box-shadow: 0 2px 6px rgba(0,0,0,0.12);
  }
  .card--olive { left: 50px; --accent: var(--olive); }
  .card--saddle { left: 630px; --accent: var(--saddle); }
  .card__band {
    position: absolute;
    left: 0; bottom: 0;
    width: 100%; height: 180px;
  }
  .card__band path { fill: var(--accent); }
  .brand {
    position: absolute;
    left: 0; right: 0;
    top: 92px;
    text-align: center;
    color: var(--accent);
    font-weight: 600;
  }
  .brand__name {
    display: inline-flex;
    align-items: center;
    gap: 12px;
    font-size: 52px;
    line-height: 1;
    letter-spacing: -0.5px;
  }
  .brand__dot {
    width: 18px; height: 18px;
    border-radius: 50%;
    background: var(--accent);
  }
  .brand__sub {
    margin-top: 8px;
    font-size: 15px;
    letter-spacing: 3px;
    text-transform: uppercase;
  }
  .contact {
    position: absolute;
    left: 44px;
    bottom: 30px;
    color: var(--band-text);
    font-size: 17px;
    line-height: 1.4;
    letter-spacing: 2px;
    text-transform: uppercase;
  }
</style>
</head>
<body>

  <section class="card card--olive">
    <div class="brand">
      <div class="brand__name"><span class="brand__dot"></span>Fern Hollow</div>
      <div class="brand__sub">Soapworks, LLC</div>
    </div>
    <svg class="card__band" viewBox="0 0 520 180" preserveAspectRatio="none" aria-hidden="true">
      <path d="M0 100 C 150 85, 300 110, 400 70 S 500 10, 520 0 L 520 180 L 0 180 Z"/>
    </svg>
    <address class="contact" style="font-style:normal">
      info@fernhollowsoap.com<br>
      P.O. Box Elmford | Virginia 22190
    </address>
  </section>

  <section class="card card--saddle">
    <div class="brand">
      <div class="brand__name"><span class="brand__dot"></span>Fern Hollow</div>
      <div class="brand__sub">Soapworks, LLC</div>
    </div>
    <svg class="card__band" viewBox="0 0 520 180" preserveAspectRatio="none" aria-hidden="true">
      <path d="M0 100 C 150 85, 300 110, 400 70 S 500 10, 520 0 L 520 180 L 0 180 Z"/>
    </svg>
    <address class="contact" style="font-style:normal">
      info@fernhollowsoap.com<br>
      P.O. Box Elmford | Virginia 22190
    </address>
  </section>

</body>
</html>
```